Hi
Thank you for considering my job.

I need a layout design for a website. The design should preferably suit GainsLayout Blogcraft layout. Please design according to the attached LAYOUT.GIF

I already have a logo which I like but could be pushed to change if you have an exceptional design. Otherwise I would like to try to incorporate the jigsaw pieces in the design somehow.

Our company is based in Australia and called Parting Toolbox. We have developed a "Sever Pack" to assist both men and women going through divorce to prepare themselves adequately before the seek legal or financial advice to ensure they pay professionals for "advice" and not instructions on basic administration.

I hope the successful candidate will also be able to design a logo and squeeze page and all of the marketing images I will need to accompany The Sever Pack in a few weeks time, though it is not part of this job.

I have attached a very rough guide as to the types of elements and how I would like it to feel. I am not set on any of the fonts or general presentation at all. I feel comfortable with the colour scheme but again, open to ideas. Although the logo has the dark teal green background, I am not sure this works on the web page - open to ideas.

Some must haves:
a video on the front page
an opt in/members' login
link to Orinoco books sales (affiliate widget)
Disclaimer must be visible on first SCREEN

The website must portray a professional, trustworthy and up to date type image - similar to a law firm, accounting firm, bank or university. It must be clean and crisp, inviting and non-gender biased.

Please message me if you have any questions at all.

Thanks again.
Marguerite
Perth, Australia

Target Market(s)

Australian MEN AND WOMEN - 30 - 60 years middle to upper income earners

Industry/Entity Type

Accounting

Requirements
Must have
• Some must haves:
a video on the front page
an opt in/members' login

The website must portray a professional, trustworthy and up to date type image - similar to a law firm, accounting firm BUT SLIGHTLY MORE PEOPLE ORIENTED

```html
<!DOCTYPE html>
<html lang="en">
<head>
<meta charset="utf-8">
<title>Parting Toolbox — Home</title>
<link href="https://fonts.googleapis.com/css2?family=PT+Sans:wght@400;700&family=Jost:wght@400;500;600&family=Questrial&display=swap" rel="stylesheet">
<style>
:root{
  --page:#e8e8e8;
  --teal:#0c5662;
  --teal-dark:#083f49;
  --cyan:#2cb8d4;
  --cyan-text:#3cc3dc;
  --panel:#f7f7f7;
  --gutter:#e4e4e4;
  --ink:#333;
  --muted:#555;
  --red:#e2380f;
  --lime:#c6e42c;
  --white:#fff;
}
*{box-sizing:border-box;margin:0;padding:0}
html,body{width:960px;height:1200px;overflow:hidden;background:var(--page)}
body{position:relative;font-family:"PT Sans",sans-serif;color:var(--ink)}
.abs{position:absolute}
.site-header{left:70px;top:0;width:820px;height:116px;background:linear-gradient(180deg,#0e5c68,#0a4b56)}
.brand{left:90px;top:56px;color:var(--white);font-family:"Questrial",sans-serif;font-size:24px;display:flex;align-items:center;gap:8px;white-space:nowrap}
.brand-mark{width:18px;height:18px;background:var(--lime)}
.brand-tag{left:90px;top:84px;color:#cfe6ea;font-family:"PT Sans",sans-serif;font-size:10px;letter-spacing:.3px}
.teaser{left:302px;top:30px;width:300px;text-align:center;color:var(--white);font-size:14.5px;line-height:17px}
.field{height:18px;background:var(--white);border-radius:4px;color:#999;font-size:10px;padding:3px 8px}
.login-btn{left:822px;top:18px;width:56px;height:19px;background:var(--lime);border-radius:3px;color:#0a3d45;font-size:12.5px;text-align:center;line-height:19px}
.login-note{left:621px;top:43px;color:var(--white);font-size:10px;line-height:14.5px}
.login-note u{color:var(--white)}
.remember{left:798px;top:48px;color:var(--white);font-size:10px;display:flex;align-items:center;gap:5px}
.remember i{width:8px;height:8px;background:var(--white);display:block}
.search{left:704px;top:78px;width:181px;height:23px;border-radius:12px;background:var(--white);color:#999;font-size:10.5px;padding:5px 12px}
.search svg{position:absolute;right:8px;top:4px}
.main-nav{left:70px;top:116px;width:820px;height:34px;background:var(--cyan)}
.main-nav a{position:absolute;top:10px;color:var(--white);font-size:11.5px;text-decoration:none;white-space:nowrap}
.curl{width:12px;height:12px;background:var(--teal-dark)}
.content{left:82px;top:150px;width:549px;height:890px;background:var(--panel)}
.gutter{left:631px;top:150px;width:14px;height:890px;background:var(--gutter)}
.sidebar{left:645px;top:150px;width:233px;height:890px;background:var(--panel)}
.invite{left:82px;top:176px;width:545px;text-align:center;font-family:"Jost",sans-serif;font-weight:600;font-size:26px;line-height:29px}
.invite .hot{color:var(--red)}
.invite .rest{color:#444}
.video-frame{left:122px;top:246px;width:455px;height:280px;background:var(--white);box-shadow:0 14px 10px -10px rgba(0,0,0,.18)}
.video{left:132px;top:256px;width:433px;height:262px;background:#000}
.video-still{left:140px;top:288px;width:416px;height:196px;background:linear-gradient(90deg,#3d3d46,#7a5a3c 30%,#d9cdbf 50%,#7a4a2c 70%,#7a1d12)}
.feature-note{left:82px;top:558px;width:545px;text-align:center;font-family:"Questrial",sans-serif;font-size:20px;line-height:24px;color:#222}
.divider{height:1px;background:#e2e2e2}
.about-title{left:82px;top:650px;width:556px;text-align:center;font-family:"Questrial",sans-serif;font-size:30px;line-height:36px;color:var(--cyan-text)}
.about-title b{font-family:"Jost",sans-serif;font-weight:600}
.about-copy{left:114px;top:701px;width:487px;text-align:center;font-family:"Questrial",sans-serif;font-size:11.4px;line-height:16px;color:var(--muted)}
.about-copy p+p{margin-top:16px}
.photo-frame{left:166px;top:818px;width:381px;height:166px;background:var(--white)}
.photo{left:174px;top:826px;width:365px;height:152px;background:linear-gradient(160deg,#f2f4f6,#b9c6d4 60%,#eef1f4)}
.steps{left:658px;top:176px;width:213px;height:62px;border:1px solid #bfe6ef;border-radius:4px;background:linear-gradient(#eaf7fb,#cfeef6)}
.step{position:absolute;top:4px;width:60px;text-align:center;color:var(--cyan);font-family:"Jost",sans-serif;font-weight:600;font-size:13px;line-height:13px}
.step small{display:block;font-size:7px;line-height:9px}
.step svg{display:block;margin:0 auto 2px}
.book{left:682px;top:282px;width:120px;height:98px;background:linear-gradient(135deg,#1d7484,#0b4752 60%,#d9d9d9)}
.price{left:784px;top:248px;color:var(--red);font-family:"PT Sans",sans-serif;font-size:26px;line-height:30px}
.hot-badge{left:800px;top:288px;width:52px;height:52px;border-radius:50%;background:var(--red)}
.buy{left:786px;top:382px;color:#d61d12;font-family:"Jost",sans-serif;font-weight:600;font-size:14px}
.blurb{left:658px;top:413px;width:214px;font-family:"Questrial",sans-serif;font-size:10.3px;line-height:14.4px;color:#222}
.details-btn{left:657px;top:494px;width:86px;height:24px;border-radius:12px;background:var(--teal);border:2px solid var(--cyan);color:var(--white);font-size:11px;text-align:center;line-height:20px;font-weight:700}
.shelf{left:654px;top:574px;width:212px;height:64px;background:linear-gradient(90deg,#7b8a99,#2f3b55 35%,#c7a24a 50%,#2b2f38 70%,#3f7070)}
.shelf-arrow{width:16px;height:8px;border-radius:3px;background:#d7d7d7}
.topics{left:668px;top:701px;list-style:none;font-size:10.5px;color:#333}
.topics li{height:24px;display:flex;align-items:center;gap:7px}
.topics li::before{content:"";border-left:4px solid #555;border-top:3px solid transparent;border-bottom:3px solid transparent}
.site-footer{left:70px;top:1040px;width:820px;height:160px;background:linear-gradient(180deg,#0b5562,#0a4753)}
.footer-text{left:70px;width:820px;text-align:center;color:var(--white);font-size:11.5px}
.footer-text span{margin:0 8px}
.copyright{left:81px;top:1172px;color:var(--white);font-size:11.5px}
.legal-links{right:76px;top:1172px;color:var(--white);font-size:11.5px}
</style>
</head>
<body>

<header class="abs site-header"></header>
<div class="abs brand"><span class="brand-mark"></span>partingtoolbox</div>
<div class="abs brand-tag">guidance for every step you take</div>
<div class="abs teaser">And this could be scrolling<br>information - testimonials and such.<br>to entice the person to stay on the website</div>

<div class="abs field" style="left:617px;top:18px;width:92px">Username</div>
<div class="abs field" style="left:719px;top:18px;width:92px">Password</div>
<div class="abs login-btn">Login</div>
<div class="abs login-note">Forgot login?<br>No account yet? <u>Register</u></div>
<div class="abs remember"><i></i>Remember me</div>
<div class="abs search">Enter Keyword
  <svg width="15" height="15" viewBox="0 0 15 15"><circle cx="6" cy="6" r="4.5" fill="none" stroke="#111" stroke-width="1.8"/><line x1="9.4" y1="9.4" x2="14" y2="14" stroke="#111" stroke-width="2.2"/></svg>
</div>

<nav class="abs main-nav">
  <a style="left:18px">Home</a>
  <a style="left:82px">Considering Divorce?</a>
  <a style="left:223px">Legal Process</a>
  <a style="left:326px">Parenting</a>
  <a style="left:409px">Property &amp; Finance</a>
  <a style="left:540px">Community</a>
  <a style="left:635px">Tools</a>
  <a style="left:700px">Faqs</a>
  <a style="left:759px">About Us</a>
</nav>
<div class="abs curl" style="left:70px;top:150px;border-radius:0 0 0 12px"></div>
<div class="abs curl" style="left:878px;top:150px;border-radius:0 0 12px 0"></div>

<main class="abs content"></main>
<div class="abs gutter"></div>
<aside class="abs sidebar"></aside>

<h1 class="abs invite"><span class="hot">Some text here to invite people to play</span><br><span class="rest">the video guide to the site</span></h1>

<div class="abs video-frame"></div>
<div class="abs video"></div>
<div class="abs video-still" role="img" aria-label="Video still of a presenter welcoming visitors to the site"></div>
<svg class="abs" style="left:313px;top:367px" width="70" height="38" viewBox="0 0 70 38"><rect width="70" height="38" rx="9" fill="#1a1a1a" fill-opacity=".85"/><path d="M29 11 L45 19 L29 27Z" fill="#fff"/></svg>

<p class="abs feature-note">This section here is for a window which<br>scrolls with feature articles.</p>
<div class="abs divider" style="left:96px;top:636px;width:520px"></div>

<h2 class="abs about-title">Parting<b>Toolbox</b></h2>
<div class="abs about-copy">
  <p>Lorem Ipsum is simply dummy text of the printing and typesetting industry. Lorem Ipsum has been the industry's standard dummy text ever since the 1500s,</p>
  <p>when an unknown printer took a galley of type and scrambled it to make a type specimen book. It has survived not only five centuries, but also the leap into electronic typesetting, remaining essentially unchanged.</p>
</div>
<div class="abs photo-frame"></div>
<div class="abs photo" role="img" aria-label="Close-up photo of a tax form"></div>

<div class="abs steps">
  <div class="step" style="left:8px"><svg width="20" height="22" viewBox="0 0 20 22"><circle cx="10" cy="11" r="10" fill="#2cb8d4"/><text x="10" y="17" text-anchor="middle" font-size="16" font-weight="700" fill="#fff" font-family="PT Sans">?</text></svg>Ask<small>a Question</small></div>
  <div class="step" style="left:76px"><svg width="20" height="22" viewBox="0 0 20 22"><circle cx="10" cy="7" r="6" fill="#f5c77a"/><rect x="3" y="13" width="14" height="9" rx="4" fill="#7ccbe3"/></svg>Expert<small>Answers</small></div>
  <div class="step" style="left:150px"><svg width="22" height="22" viewBox="0 0 22 22"><circle cx="11" cy="11" r="10.5" fill="#f7d53a"/><path d="M6 12 Q11 17 16 12" stroke="#b8860b" stroke-width="1.5" fill="none"/></svg>Accept<small>if Satisfied</small></div>
  <svg class="abs" style="left:56px;top:12px" width="26" height="16" viewBox="0 0 26 16"><path d="M2 2 L9 8 L2 14 M12 2 L19 8 L12 14" stroke="#bfe6ef" stroke-width="3" fill="none"/></svg>
  <svg class="abs" style="left:132px;top:12px" width="26" height="16" viewBox="0 0 26 16"><path d="M2 2 L9 8 L2 14 M12 2 L19 8 L12 14" stroke="#bfe6ef" stroke-width="3" fill="none"/></svg>
</div>

<div class="abs book" role="img" aria-label="Cover of the downloadable separation guide"></div>
<div class="abs hot-badge" role="img" aria-label="Hot price badge"></div>
<div class="abs price">$12.99</div>
<div class="abs buy">BUY NOW</div>
<p class="abs blurb">Download immediately.This simple guide provides a wealth of essential information and answers to your questions. Advice and tips to help you get a grip on all the changes in your life.</p>
<div class="abs details-btn">More Details</div>

<div class="abs shelf" role="img" aria-label="Bookstore affiliate carousel of book covers"></div>
<div class="abs shelf-arrow" style="left:826px;top:630px"></div>
<div class="abs shelf-arrow" style="left:848px;top:630px"></div>
<div class="abs divider" style="left:654px;top:680px;width:216px"></div>

<ul class="abs topics">
  <li>Ask Our Experts</li><li>After Divorce</li><li>Avoiding Divorce</li><li>Considering Divorce</li>
  <li>Dependants</li><li>Facts &amp; Figures</li><li>Finances</li><li>Getting Help</li>
  <li>Going Through Divorce</li><li>New Relationships</li><li>Property</li><li>Separation Agreements</li>
</ul>

<footer class="abs site-footer"></footer>
<div class="abs curl" style="left:70px;top:1028px;border-radius:12px 0 0 0"></div>
<div class="abs curl" style="left:878px;top:1028px;border-radius:0 12px 0 0"></div>
<div class="abs footer-text" style="top:1075px">Home<span>|</span>Considering Divorce?<span>|</span>Legal Process<span>|</span>Parenting<span>|</span>Property &amp; Finance<span>|</span>Community<span>|</span>Tools<span>|</span>Faqs<span>|</span>About Us</div>
<div class="abs footer-text" style="top:1095px">Legal Disclaimer.</div>
<div class="abs footer-text" style="top:1114px">I suppose there is standard tabular information down here</div>
<div class="abs copyright">© PartingToolbox 2000-2013</div>
<div class="abs legal-links">Terms &amp; Conditions &nbsp;| &nbsp;Privacy Policy</div>

</body>
</html>
```